A webite for an Urgent Care for children

We need a design for a new website for an Urgent care for kids. We are based in Atlanta, GA and provide quality after-hours and urgent care services for children. We will appreciate an innovative design that employs flash technology, especially on the Home page. We also want there to be a Contact Us form. There should also be a control panel with the ability for us to make quick and minor edits on the website as needed without requiring the services of an expert.

Target Market(s)

Parents, children, general audience

Industry/Entity Type

Healthcare

Coding

Coded - Design and coding required

Number of Pages Required

5+ page

Font styles to use
Sans Serif
Decorative

Colors
acd037
acd136
cadf82
eaf2ce
f6faec

Requirements
Must have
• Mobile devices website capable
• Link to social media, Facebook, twitter, etc
Nice to have
• Ability for customers to pay online.

```html
<!DOCTYPE html>
<html lang="en">
<head>
<meta charset="utf-8">
<title>Sunnyhop Urgent Care</title>
<link href="https://fonts.googleapis.com/css2?family=Fredoka:wght@700&family=Kalam:wght@400;700&family=Oswald:wght@400&family=Open+Sans:wght@400;600&display=swap" rel="stylesheet">
<style>
:root{
  --green:#acd037;
  --green-2:#acd136;
  --green-soft:#cadf82;
  --green-pale:#eaf2ce;
  --green-bg:#f6faec;
  --ink:#1d1d1d;
  --text:#333;
  --star:#f2b600;
  --sky-top:#17658f;
  --sky-mid:#2f8fb8;
  --title:#fde637;
  --white:#fff;
  --black:#111;
}
*{box-sizing:border-box;margin:0;padding:0}
html,body{width:1200px;height:2456px;overflow:hidden}
body{position:relative;background:var(--white);font-family:"Open Sans",sans-serif;color:var(--text)}
.abs{position:absolute}

/* header */
.hero{left:0;top:0;width:1200px;height:300px;background:linear-gradient(180deg,var(--sky-top) 0%,var(--sky-mid) 70%,#8bc34a 86%,var(--green) 100%)}
.topbar{left:65px;top:6px;right:65px;height:24px;display:flex;justify-content:space-between;align-items:center;color:var(--white);font-size:12px}
.cart{display:flex;align-items:center;gap:6px}
.social{display:flex;gap:9px}
.social span{width:11px;height:11px;border-radius:50%;background:var(--white);display:block}
.site-title{left:0;width:1200px;top:96px;text-align:center;font-family:"Fredoka",sans-serif;font-weight:700;font-size:50px;color:var(--title);letter-spacing:.5px}
.nav{left:0;top:300px;width:1200px;height:50px;background:var(--green);display:flex;justify-content:center;align-items:center;gap:54px;font-family:"Oswald",sans-serif;font-size:19px;color:var(--ink)}

/* welcome */
.section-title{left:0;width:1200px;text-align:center;font-family:"Kalam",cursive;font-weight:400;font-size:50px;color:var(--ink)}
.section-title em{font-style:normal;color:var(--green)}
.welcome-title{top:378px}
.welcome-text{left:125px;width:950px;top:462px;text-align:center;font-size:13.5px;line-height:28px;color:var(--text)}
.welcome-text p+p{margin-top:18px}
.btn{display:flex;align-items:center;justify-content:center;font-size:15px;color:var(--ink)}
.btn-welcome{left:502px;top:728px;width:196px;height:38px;background:var(--green)}

/* featured */
.featured-title{top:825px}
.featured-sub{left:0;width:1200px;top:905px;text-align:center;font-size:12px;color:#777}
.featured-rule{left:585px;top:932px;width:30px;height:2px;background:var(--green)}
.card{width:253px;height:362px;border:2px solid var(--green-soft);background:var(--white)}
.card-media{position:absolute;left:0;top:0;right:0;height:250px;border-bottom:2px solid var(--green-soft)}
.card-media .ph{position:absolute;left:50%;top:50%;width:150px;height:130px;transform:translate(-50%,-50%);border-radius:18px}
.ph-laptop{background:linear-gradient(160deg,#e74a3b,#2a4aa8)}
.ph-train{background:linear-gradient(90deg,#e53935,#43a047 50%,#fbc02d);height:70px!important}
.ph-rattle{background:linear-gradient(180deg,#8bc34a,#e0e0e0 60%,#6a3fa0)}
.ph-car{background:linear-gradient(180deg,#f56a80,#f8a8b4);border-radius:50px!important;height:110px!important}
.badge{position:absolute;left:0;top:0;background:var(--green);color:var(--white);font-size:10px;letter-spacing:.5px;padding:2px 6px;text-transform:uppercase}
.actions{position:absolute;right:8px;top:144px;display:flex;flex-direction:column;gap:5px}
.actions span{width:26px;height:26px;background:var(--green);display:flex;align-items:center;justify-content:center}
.card-body{position:absolute;left:0;right:0;top:250px;bottom:0;background:var(--green-bg);padding:22px 18px 0}
.card-name{font-size:15px;color:var(--ink)}
.card-foot{display:flex;justify-content:space-between;align-items:center;margin-top:20px}
.price{background:var(--green);font-size:12px;color:var(--ink);padding:3px 10px}
.stars{color:var(--star);font-size:11px;letter-spacing:3px}

/* footer */
.footer-art{left:0;top:1800px;width:1200px;height:80px;background:linear-gradient(90deg,#2a9d8f,#e65100 20%,#fbc02d 40%,#d84315 60%,#fbc02d 80%,#e65100)}
.footer-wave{left:0;top:1820px;width:1200px;height:60px}
.footer{left:0;top:1870px;width:1200px;height:533px;background:var(--green)}
.foot-h{font-family:"Kalam",cursive;font-size:23px;color:var(--white);letter-spacing:.5px}
.pay{left:130px;width:380px;top:1940px;text-align:center}
.pay-row{display:flex;justify-content:center;gap:8px;margin-top:20px}
.pay-row span{width:34px;height:20px;border:1.5px solid var(--white);border-radius:3px;opacity:.9}
.avail{left:690px;width:480px;top:1940px;text-align:center}
.avail-row{display:flex;justify-content:center;gap:40px;margin-top:18px;color:var(--white);font-size:17px}
.avail-row span{display:flex;align-items:center;gap:8px}
.divider{left:65px;top:2066px;width:1053px;height:1px;background:rgba(255,255,255,.55)}
.col{top:2105px}
.col .foot-h{font-size:22px;margin-bottom:12px}
.col-about{left:65px;width:320px}
.col-about p{font-size:11.5px;line-height:22px;color:var(--ink)}
.links{list-style:none;font-size:13px;color:var(--ink)}
.links li{height:33px}
.col-links{left:463px}
.col-contact{left:692px}
.col-shop{left:943px}
.contact li{display:flex;align-items:center;gap:10px}
.foot-social{display:flex;gap:17px;margin-top:12px}
.foot-social span{width:10px;height:10px;border-radius:50%;background:var(--ink)}
.btn-foot{left:65px;top:2333px;width:84px;height:33px;background:var(--black);color:var(--white);font-size:12px}
.copyright{left:0;top:2403px;width:1200px;height:53px;background:var(--black);color:var(--white);font-size:13px;display:flex;align-items:center;justify-content:center}
</style>
</head>
<body>

<header class="abs hero" role="img" aria-label="Cartoon sky with clouds, toy train, rocking horse, toy car and teddy bear on grass"></header>
<div class="abs topbar">
  <div class="cart">
    <svg width="14" height="12" viewBox="0 0 14 12"><path d="M0 1h2.5l2 7h7l1.5-5H4" fill="none" stroke="#fff" stroke-width="1.3"/><circle cx="5.5" cy="10.5" r="1" fill="#fff"/><circle cx="10.5" cy="10.5" r="1" fill="#fff"/></svg>
    Cart Items : 1
  </div>
  <div class="social"><span></span><span></span><span></span><span></span><span></span><span></span></div>
</div>
<div class="abs site-title">Sunnyhop Urgent Care</div>

<nav class="abs nav">
  <span>Home</span><span>About Us</span><span>Our Services</span><span>Finance and Insurance</span><span>Office Forms</span><span>Contact Us</span><span>FAQ</span>
</nav>

<h1 class="abs section-title welcome-title">Welcome to <em>Sunnyhop</em></h1>
<div class="abs welcome-text">
  <p>He attended the renowned Lakeside College of Medicine, where he obtained his medical degree. As Chief Steward, head of the largest student service society on his campus, his philanthropic activities included helping fellow students in need. In the early days of his career, he collaborated with the Global Health Alliance and the national government in combating an outbreak of yellow fever in some rural communities during his National Service. He is married to Kemi, an accountant, and together they have three lovely children.</p>
  <p>Dr. Adeyemi and his family spent five years in Columbia, Missouri, during which time he also completed his residency in Pediatrics at Riverbend University Hospital. His desire was to work with Christian believers and was led to the Atlanta area where he teamed up with a group of pediatricians in Fayetteville for two years.</p>
</div>
<div class="abs btn btn-welcome">Read More</div>

<h2 class="abs section-title featured-title">Featured <em>Items</em></h2>
<div class="abs featured-sub">Listed below our best seller items with carousel widget</div>
<div class="abs featured-rule"></div>

<!-- row 1 -->
<div class="abs card" style="left:65px;top:994px">
  <div class="card-media"><div class="ph ph-laptop" role="img" aria-label="Toy learning laptop"></div><span class="badge">Best selling</span>
    <div class="actions">
      <span><svg width="12" height="10" viewBox="0 0 14 12"><path d="M0 1h2.5l2 7h7l1.5-5H4" fill="none" stroke="#fff" stroke-width="1.6"/></svg></span>
      <span><svg width="12" height="11" viewBox="0 0 12 11"><path d="M6 10 1.5 5.5A2.6 2.6 0 0 1 6 2a2.6 2.6 0 0 1 4.5 3.5Z" fill="none" stroke="#fff" stroke-width="1.4"/></svg></span>
      <span><svg width="13" height="9" viewBox="0 0 13 9"><path d="M.5 4.5Q6.5-2 12.5 4.5Q6.5 11 .5 4.5Z" fill="none" stroke="#fff" stroke-width="1.3"/><circle cx="6.5" cy="4.5" r="1.6" fill="#fff"/></svg></span>
    </div>
  </div>
  <div class="card-body"><div class="card-name">Nullami tincidunte</div><div class="card-foot"><span class="price">$80.00</span><span class="stars">★★★★★</span></div></div>
</div>
<div class="abs card" style="left:333px;top:994px">
  <div class="card-media"><div class="ph ph-train" role="img" aria-label="Toy block train"></div></div>
  <div class="card-body"><div class="card-name">Malesuada mi</div><div class="card-foot"><span class="price">$40.00</span><span class="stars">★★★★★</span></div></div>
</div>
<div class="abs card" style="left:600px;top:994px">
  <div class="card-media"><div class="ph ph-rattle" role="img" aria-label="Baby activity toy"></div></div>
  <div class="card-body"><div class="card-name">Phasellus a arcua</div><div class="card-foot"><span class="price">$20.00</span><span class="stars">★★★★★</span></div></div>
</div>
<div class="abs card" style="left:866px;top:994px">
  <div class="card-media"><div class="ph ph-car" role="img" aria-label="Pink toy car"></div><span class="badge">Best selling</span></div>
  <div class="card-body"><div class="card-name">Curabitur sodales</div><div class="card-foot"><span class="price">$140.00</span><span class="stars">★★★★★</span></div></div>
</div>

<!-- row 2 -->
<div class="abs card" style="left:65px;top:1372px">
  <div class="card-media"><div class="ph ph-rattle" role="img" aria-label="Baby activity toy"></div><span class="badge">Best selling</span></div>
  <div class="card-body"><div class="card-name">Nullami tincidunte</div><div class="card-foot"><span class="price">$80.00</span><span class="stars">★★★★★</span></div></div>
</div>
<div class="abs card" style="left:333px;top:1372px">
  <div class="card-media"><div class="ph ph-car" role="img" aria-label="Pink toy car"></div></div>
  <div class="card-body"><div class="card-name">Malesuada mi</div><div class="card-foot"><span class="price">$40.00</span><span class="stars">★★★★★</span></div></div>
</div>
<div class="abs card" style="left:600px;top:1372px">
  <div class="card-media"><div class="ph ph-laptop" role="img" aria-label="Toy learning laptop"></div><span class="badge">Best selling</span></div>
  <div class="card-body"><div class="card-name">Phasellus a arcua</div><div class="card-foot"><span class="price">$20.00</span><span class="stars">★★★★★</span></div></div>
</div>
<div class="abs card" style="left:866px;top:1372px">
  <div class="card-media"><div class="ph ph-train" role="img" aria-label="Toy block train"></div></div>
  <div class="card-body"><div class="card-name">Curabitur sodales</div><div class="card-foot"><span class="price">$140.00</span><span class="stars">★★★★★</span></div></div>
</div>

<!-- footer -->
<div class="abs footer-art" role="img" aria-label="Row of colourful toys: pyramid, ball, puzzle pieces, rocking horse, letter blocks and clock"></div>
<svg class="abs footer-wave" viewBox="0 0 1200 60" preserveAspectRatio="none"><path d="M0 30Q150 5 300 28T600 25T900 30T1200 22V60H0Z" fill="#acd037"/></svg>
<footer class="abs footer"></footer>

<div class="abs pay">
  <div class="foot-h">Payment Methods</div>
  <div class="pay-row"><span></span><span></span><span></span><span></span><span></span><span></span></div>
</div>
<div class="abs avail">
  <div class="foot-h">We're Available 24/7</div>
  <div class="avail-row">
    <span><svg width="16" height="16" viewBox="0 0 16 16"><path d="M3 1l3 3-1.5 2a9 9 0 0 0 5.5 5.5L12 10l3 3-2 2C6 14 2 10 1 3Z" fill="#fff"/></svg>+1 555 014 2267</span>
    <span><svg width="20" height="16" viewBox="0 0 20 16"><rect x="1" y="5" width="18" height="10" rx="2" fill="#fff"/><rect x="5" y="1" width="10" height="5" fill="#fff"/></svg>+1 555 014 6677</span>
  </div>
</div>
<div class="abs divider"></div>

<div class="abs col col-about">
  <div class="foot-h">We Are Urgent Care</div>
  <p>Welcome to Sunnyhop Urgent Care, your after-hours pediatric urgent care. We are here when your little ones suddenly wake up sick or sustain an injury and you need immediate medical attention, but your regular doctor's office is closed. We are unique in the services we provide and are an alternative when your child needs.</p>
</div>
<div class="abs col col-links">
  <div class="foot-h">Main Links</div>
  <ul class="links"><li>Home</li><li>About Us</li><li>Our Services</li><li>Office Forms</li><li>Contact Us</li></ul>
</div>
<div class="abs col col-contact">
  <div class="foot-h">Get In Touch</div>
  <ul class="links contact">
    <li><svg width="13" height="10" viewBox="0 0 13 10"><rect x=".5" y=".5" width="12" height="9" fill="#1d1d1d"/><path d="M.5.5 6.5 5l6-4.5" stroke="#acd037" fill="none"/></svg>info@sunnyhopcare.com</li>
    <li><svg width="12" height="12" viewBox="0 0 16 16"><path d="M3 1l3 3-1.5 2a9 9 0 0 0 5.5 5.5L12 10l3 3-2 2C6 14 2 10 1 3Z" fill="#1d1d1d"/></svg>+1 555 014 4578</li>
    <li><svg width="13" height="13" viewBox="0 0 13 13"><path d="M5 8 8 5M4 6 2 8a2 2 0 0 0 3 3l2-2M9 7l2-2a2 2 0 0 0-3-3L6 4" stroke="#1d1d1d" stroke-width="1.5" fill="none"/></svg>www.sunnyhopcare.com</li>
  </ul>
  <div class="foot-social"><span></span><span></span><span></span><span></span><span></span><span></span></div>
</div>
<div class="abs col col-shop">
  <div class="foot-h">Main Links</div>
  <ul class="links"><li>Delivery Time</li><li>Order Tracking</li><li>Shopping Cart</li><li>My Account</li><li>Secure Payment</li></ul>
</div>
<div class="abs btn btn-foot">Read More</div>

<div class="abs copyright">Copyright © 2016 sunnyhopurgentcare | All Rights Reserved</div>

</body>
</html>
```